Bref créative
Brisk Lattice Cards & Stationary
Project #2
Corporate
Carl Wendimeer
VP of Business Development
2841 Thornbury Lane
Lindmoor, MN 55612
cwendimeer@brisklattice-mail.com
www.brisklattice-mail.com
Here is our logo

```html
<!DOCTYPE html>
<html lang="en">
<head>
<meta charset="utf-8">
<title>Brisk Lattice Stationery</title>
<link rel="stylesheet" href="https://fonts.googleapis.com/css2?family=Montserrat:wght@400;600&display=swap">
<style>
  :root {
    --backdrop: #4b4b4b;
    --paper: #ffffff;
    --paper-edge: #e6e6e6;
    --brand-blue: #1f7fd0;
    --ink-grey: #8a8a8a;
    --accent-grey-a: #f4f4f4;
    --accent-grey-b: #d8d8d8;
  }
  * { box-sizing: border-box; margin: 0; padding: 0; }
  html, body { width: 1200px; height: 564px; overflow: hidden; }
  body {
    background: var(--backdrop);
    font-family: "Montserrat", sans-serif;
    position: relative;
  }
  .sheet {
    position: absolute;
    background: var(--paper);
    overflow: hidden;
  }
  .wordmark {
    display: flex;
    align-items: center;
    gap: 0.35em;
    color: var(--brand-blue);
    font-weight: 600;
    white-space: nowrap;
  }
  .wordmark-square {
    width: 0.9em; height: 0.9em;
    background: var(--brand-blue);
    flex: none;
  }
  .fine-print {
    position: absolute;
    font-size: 5px;
    color: var(--ink-grey);
    font-weight: 400;
    white-space: nowrap;
  }
  .corner-accent {
    position: absolute;
    background: linear-gradient(135deg, var(--accent-grey-a) 0%, var(--accent-grey-b) 60%, var(--accent-grey-a) 100%);
  }

  /* Presentation folder */
  .folder-cover { left: 60px; top: 12px; width: 252px; height: 456px; border-right: 1px solid var(--paper-edge); }
  .folder-cover .wordmark { position: absolute; left: 50%; top: 150px; transform: translateX(-50%); font-size: 26px; }
  .folder-cover .fine-print { left: 20px; bottom: 16px; }

  .folder-inside { left: 312px; top: 12px; width: 252px; height: 456px; }
  .folder-inside .wordmark { position: absolute; left: 38px; top: 186px; font-size: 20px; }
  .folder-inside .fine-print { left: 38px; bottom: 16px; color: var(--brand-blue); }
  .folder-inside .corner-accent { right: 0; bottom: 0; width: 90px; height: 130px; border-top-left-radius: 90px 130px; }

  .folder-pocket {
    left: 308px; top: 468px; width: 256px; height: 80px;
    border-bottom-left-radius: 46px;
  }
  .folder-pocket .wordmark { position: absolute; left: 96px; top: 24px; font-size: 13px; }

  /* Business card */
  .business-card { left: 91px; top: 504px; width: 96px; height: 38px; }
  .business-card .wordmark { position: absolute; left: 6px; top: 5px; font-size: 6px; }
  .business-card .fine-print { font-size: 3px; left: 6px; }

  /* Letterhead */
  .letterhead { left: 607px; top: 108px; width: 269px; height: 439px; }
  .letterhead .wordmark { position: absolute; left: 14px; top: 16px; font-size: 11px; }
  .letterhead .fine-print { left: 14px; font-size: 4px; }
  .letterhead .corner-accent { right: 0; bottom: 0; width: 70px; height: 110px; border-top-left-radius: 70px 110px; }

  /* Envelope */
  .envelope { left: 883px; top: 158px; width: 245px; height: 120px; }
  .envelope .wordmark { position: absolute; left: 50%; top: 12px; transform: translateX(-50%); font-size: 9px; }
  .envelope .window { position: absolute; left: 20px; top: 60px; width: 90px; height: 30px; border: 1px solid var(--paper-edge); }

  /* Compliment card */
  .compliment-card { left: 883px; top: 307px; width: 245px; height: 168px; }
  .compliment-card .wordmark { position: absolute; left: 14px; top: 20px; font-size: 10px; }
  .compliment-card .fine-print { left: 14px; font-size: 4px; }
  .compliment-card .corner-accent { right: 0; bottom: 0; width: 60px; height: 100px; border-top-left-radius: 60px 100px; }
</style>
</head>
<body>
  <section class="sheet folder-cover">
    <div class="wordmark"><span class="wordmark-square"></span>Brisk Lattice</div>
    <p class="fine-print">2841 Thornbury Lane, Lindmoor, MN 55612</p>
  </section>

  <section class="sheet folder-inside">
    <div class="wordmark"><span class="wordmark-square"></span>Brisk Lattice</div>
    <div class="corner-accent" role="img" aria-label="Soft grey corner accent"></div>
    <p class="fine-print">www.brisklattice-mail.com</p>
  </section>

  <section class="sheet folder-pocket">
    <div class="wordmark"><span class="wordmark-square"></span>Brisk Lattice</div>
  </section>

  <section class="sheet business-card">
    <div class="wordmark"><span class="wordmark-square"></span>Brisk Lattice</div>
    <p class="fine-print" style="top:20px">Carl Wendimeer</p>
    <p class="fine-print" style="top:25px">VP of Business Development</p>
    <p class="fine-print" style="top:30px">cwendimeer@brisklattice-mail.com</p>
  </section>

  <section class="sheet letterhead">
    <div class="wordmark"><span class="wordmark-square"></span>Brisk Lattice</div>
    <div class="corner-accent" role="img" aria-label="Soft grey corner accent"></div>
    <p class="fine-print" style="top:400px">2841 Thornbury Lane, Lindmoor, MN 55612</p>
    <p class="fine-print" style="top:407px">www.brisklattice-mail.com</p>
  </section>

  <section class="sheet envelope">
    <div class="wordmark"><span class="wordmark-square"></span>Brisk Lattice</div>
    <div class="window"></div>
  </section>

  <section class="sheet compliment-card">
    <div class="wordmark"><span class="wordmark-square"></span>Brisk Lattice</div>
    <div class="corner-accent" role="img" aria-label="Soft grey corner accent"></div>
    <p class="fine-print" style="top:128px">2841 Thornbury Lane, Lindmoor, MN 55612</p>
    <p class="fine-print" style="top:135px">www.brisklattice-mail.com</p>
  </section>
</body>
</html>
```